Real Estate Agent needs business card design

We have logo designed already, want to have business card designed. Very interested in those smaller size business card as they look very trendy. Business name is called VORENDA REALTY

```html
<!DOCTYPE html>
<html lang="en">
<head>
<meta charset="utf-8">
<title>Vorenda Realty – Business Cards</title>
<link rel="stylesheet" href="https://fonts.googleapis.com/css2?family=Cinzel:wght@500&family=Crimson+Pro:ital,wght@0,400;0,500;1,400&display=swap">
<style>
  :root {
    --backdrop: #e6e6e6;
    --charcoal: #2d2e30;
    --paper: #f4f4f3;
    --gold: #a8844f;
    --ink: #222222;
    --white: #f2f2f2;
    --muted: #444444;
  }
  * { box-sizing: border-box; margin: 0; padding: 0; }
  html, body { width: 1200px; height: 576px; overflow: hidden; }
  body {
    background: var(--backdrop);
    position: relative;
    font-family: "Crimson Pro", Georgia, serif;
  }
  .card {
    position: absolute;
    top: 138px;
    border-radius: 13px;
    overflow: hidden;
  }
  /* Front */
  .card--front {
    left: 82px; width: 485px; height: 294px;
    background: var(--charcoal);
  }
  .front__mark {
    position: absolute; left: 226px; top: 232px;
    width: 0; height: 0;
  }
  .front__square {
    position: absolute; left: 220px; top: 88px;
    width: 44px; height: 44px;
    background: var(--gold);
  }
  .front__name {
    position: absolute; left: 0; right: 0; top: 166px;
    text-align: center;
    font-family: "Cinzel", "Times New Roman", serif;
    font-weight: 500; font-size: 31px; letter-spacing: 1px;
    color: var(--white);
  }
  .front__web {
    position: absolute; left: 0; right: 0; top: 256px;
    text-align: center;
    font-size: 14px; letter-spacing: 4.6px;
    color: var(--white);
  }
  /* Back */
  .card--back {
    left: 602px; width: 482px; height: 292px;
    background: var(--paper);
  }
  .back__brand {
    position: absolute; left: 34px; top: 44px;
    display: flex; align-items: center; gap: 18px;
  }
  .back__square {
    width: 40px; height: 40px; background: var(--gold);
  }
  .back__name {
    font-family: "Cinzel", "Times New Roman", serif;
    font-weight: 500; font-size: 28px; letter-spacing: 0.5px;
    color: var(--ink);
  }
  .agent {
    position: absolute; left: 34px; top: 216px;
  }
  .agent__name {
    font-size: 22px; font-weight: 500; color: var(--gold); line-height: 1.1;
  }
  .agent__role {
    font-size: 12px; font-style: italic; color: var(--ink);
  }
  .contact {
    position: absolute; left: 272px; top: 171px;
    font-size: 13.5px; color: var(--ink); line-height: 16px;
  }
  .contact__address { margin-bottom: 12px; }
  .contact__row { display: flex; align-items: center; gap: 8px; }
  .contact__row svg { width: 10px; height: 10px; fill: var(--muted); }
  .back__bands { position: absolute; left: 0; bottom: 0; width: 482px; height: 32px; }
  .back__web {
    position: absolute; left: 272px; bottom: 7px;
    font-size: 13.5px; color: var(--white);
  }
  .back__web .domain { color: var(--gold); }
</style>
</head>
<body>
  <section class="card card--front" aria-label="Card front">
    <div class="front__square"></div>
    <div class="front__name">Vorenda Realty</div>
    <div class="front__web">www.vorendarealty.com.au</div>
  </section>

  <section class="card card--back" aria-label="Card back">
    <div class="back__brand">
      <div class="back__square"></div>
      <div class="back__name">Vorenda Realty</div>
    </div>

    <div class="agent">
      <div class="agent__name">Hannah Liang</div>
      <div class="agent__role">Senior Property Consultant</div>
    </div>

    <div class="contact">
      <div class="contact__address">7C, 48 Harbour Parade,<br>Eastwood Bay, NSW 2190</div>
      <div class="contact__row">
        <svg viewBox="0 0 10 10"><path d="M1 3.5C1 2 2.5 1 5 1s4 1 4 2.5v1H7V3.5H3v1H1z M2.5 5h5l1 4h-7z"/></svg>
        <span>0412 555 019</span>
      </div>
      <div class="contact__row">
        <svg viewBox="0 0 10 10"><path d="M5 0.5a4.5 4.5 0 1 0 0 9a4.5 4.5 0 1 0 0-9zm0 1c.6 0 1.3 1.2 1.5 3H3.5C3.7 2.7 4.4 1.5 5 1.5zM1.6 5.5h1.9c.1 1.2.4 2.2.8 2.9A3.5 3.5 0 0 1 1.6 5.5zm0-1a3.5 3.5 0 0 1 2.7-2.9c-.4.7-.7 1.7-.8 2.9zm3.4 4c-.6 0-1.3-1.2-1.5-3h3c-.2 1.8-.9 3-1.5 3zm.7-.1c.4-.7.7-1.7.8-2.9h1.9a3.5 3.5 0 0 1-2.7 2.9zm.8-3.9c-.1-1.2-.4-2.2-.8-2.9a3.5 3.5 0 0 1 2.7 2.9z"/></svg>
        <span>info@vorendarealty.com.au</span>
      </div>
    </div>

    <svg class="back__bands" viewBox="0 0 482 32" aria-hidden="true">
      <rect x="0" y="20" width="260" height="12" fill="var(--gold)"/>
      <polygon points="272,0 482,0 482,32 242,32" fill="var(--charcoal)"/>
    </svg>
    <div class="back__web">www.<span class="domain">vorendarealty</span>.com.au</div>
  </section>
</body>
</html>
```